New Plumbing Company

We are looking for a smart and creative business card design for our new plumbing company. We are looking for creativity and originality in our business cards.

Industry/Entity Type

Plumbing

Contact Information for Business Card

Crestline Plumbing
Peter Halvane
Managing Director
Telephone Number : 0481529604
Email : service@crestlineplumbing.com.au
Website : www.crestlineplumbing.com.au
Lic. 508264K

Colors
0692cd
33a6d7
000000

Requirements
Must have
• I want the business card to be designed on a black background using the blue tones i have selected as seen in the company logo.

```html
<!DOCTYPE html>
<html lang="en">
<head>
<meta charset="utf-8">
<title>Crestline Plumbing – Business Card</title>
<link rel="stylesheet" href="https://fonts.googleapis.com/css2?family=Michroma&family=Roboto+Condensed:wght@400;700&display=swap">
<style>
  :root {
    --blue-deep: #0692cd;
    --blue-light: #33a6d7;
    --blue-dark: #0a5f96;
    --card-black: #1b1a1a;
    --ink-white: #ffffff;
    --stage: #d8d5d3;
    --photo-warm: #d9c6ad;
    --photo-cool: #b8b2ab;
  }
  html, body {
    margin: 0;
    width: 1200px;
    height: 786px;
    overflow: hidden;
    background: var(--stage);
  }
  .card {
    position: absolute;
    left: 150px;
    top: 136px;
    width: 900px;
    height: 514px;
    background: var(--card-black);
    overflow: hidden;
    font-family: "Roboto Condensed", Arial, sans-serif;
    color: var(--ink-white);
  }
  .card-art {
    position: absolute;
    inset: 0;
  }
  .brand {
    position: absolute;
    left: 62px;
    top: 52px;
    display: flex;
    align-items: center;
    gap: 14px;
  }
  .brand-mark {
    width: 40px;
    height: 40px;
    border-radius: 50%;
    background: var(--blue-deep);
  }
  .brand-name {
    font-size: 34px;
    font-weight: 400;
    color: var(--blue-light);
    letter-spacing: 0.5px;
  }
  .licence {
    position: absolute;
    left: 62px;
    top: 116px;
    font-size: 15px;
    letter-spacing: 3px;
    color: var(--blue-deep);
  }
  .contact {
    position: absolute;
    left: 62px;
    top: 160px;
    margin: 0;
    padding: 0;
    list-style: none;
    font-size: 22px;
  }
  .contact li { margin-bottom: 14px; }
  .contact-phone { letter-spacing: 9px; }
  .contact-web {
    margin-top: 22px;
    color: var(--blue-deep);
    font-weight: 700;
    letter-spacing: 1px;
  }
  .person {
    position: absolute;
    right: 60px;
    top: 188px;
    text-align: right;
  }
  .person-name {
    margin: 0;
    font-family: "Michroma", Arial, sans-serif;
    font-size: 27px;
    letter-spacing: 4px;
    text-transform: uppercase;
    color: var(--ink-white);
  }
  .person-role {
    margin: 6px 0 0;
    font-size: 18px;
    letter-spacing: 5px;
    text-transform: uppercase;
    color: var(--blue-deep);
  }
</style>
</head>
<body>
  <div class="card">
    <svg class="card-art" width="900" height="514" viewBox="0 0 900 514" aria-hidden="false">
      <defs>
        <linearGradient id="swoosh-blue" x1="0" y1="0" x2="1" y2="1">
          <stop offset="0" stop-color="var(--blue-light)"/>
          <stop offset="1" stop-color="var(--blue-dark)"/>
        </linearGradient>
        <linearGradient id="photo-tone" x1="0" y1="0" x2="1" y2="1">
          <stop offset="0" stop-color="var(--photo-warm)"/>
          <stop offset="1" stop-color="var(--photo-cool)"/>
        </linearGradient>
      </defs>
      <path class="swoosh" d="M560,0 L900,0 L900,514 L830,514 C880,360 820,120 560,0 Z" fill="url(#swoosh-blue)"/>
      <g class="drop" transform="translate(680 392)">
        <path d="M99.4,11 L113.1,-113.1 L-11,-99.4 A100,100 0 1 0 99.4,11 Z"
              fill="url(#photo-tone)" stroke="var(--blue-deep)" stroke-width="9" stroke-linejoin="round"
              role="img" aria-label="Photo of a hand tightening a pipe valve with an adjustable wrench"/>
      </g>
    </svg>

    <div class="brand">
      <span class="brand-mark"></span>
      <span class="brand-name">Crestline Plumbing</span>
    </div>
    <div class="licence">LIC. 508264K</div>

    <ul class="contact">
      <li class="contact-phone">Ph: 0481529604</li>
      <li class="contact-email">E: service@crestlineplumbing.com.au</li>
      <li class="contact-web">www.crestlineplumbing.com.au</li>
    </ul>

    <div class="person">
      <h1 class="person-name">Peter Halvane</h1>
      <p class="person-role">Managing Director</p>
    </div>
  </div>
</body>
</html>
```